Kip's Pharmacy Business Card Design Project

I need a business card designed for my pharmacy Kip's Pharmacy. I would like just the logo on one side, maybe with black background and white lettering. The other side I would also like to include my logo which is attached. Also, please include my name and the following information:
Rolf Mayhew Owner/Pharm D.
Business address is 7314 N Birchwood Rd Sioux Falls, SD 57193.
Phone number is 605-318-2067 and fax # is 605-318-2063.
my email address is kip@kipsrxhall.com.
My website is www.kipsrxhall.com.
My business hours are Monday-Friday 8am-7 pm. Saturday 8am-12 pm. Sunday Closed.
I would like the design to include my logo colors, black, white, and neon green. Silver may be added as a highlight. Thanks.
Industry/Entity Type
Pharmacy
Contact Information for Business Card
See above in product description
Look and feel

```html
<!DOCTYPE html>
<html lang="en">
<head>
<meta charset="utf-8">
<title>Kip's Pharmacy – Business Card</title>
<link rel="stylesheet" href="https://fonts.googleapis.com/css2?family=Open+Sans:wght@400;600&family=Tinos&display=swap">
<style>
  :root {
    --black: #000000;
    --panel: #121212;
    --strip: #262626;
    --neon: #9dcb3b;
    --white: #ffffff;
    --grey: #bdbdbd;
    --paper: #ffffff;
  }
  * { margin: 0; padding: 0; box-sizing: border-box; }
  html, body { width: 1200px; height: 848px; overflow: hidden; background: var(--paper); }
  body { position: relative; font-family: "Open Sans", sans-serif; color: var(--white); }

  .card { position: absolute; width: 578px; height: 333px; background: var(--black); overflow: hidden; }
  .card--front { left: 304px; top: 59px; }
  .card--back { left: 308px; top: 424px; }

  .band-green { position: absolute; left: 0; right: 0; bottom: 0; height: 30px; background: var(--neon); }

  .brand { position: absolute; display: flex; align-items: center; gap: 12px; }
  .brand__dot { width: 26px; height: 26px; border-radius: 50%; background: var(--neon); }
  .brand__name { font-weight: 600; font-size: 28px; letter-spacing: -0.5px; color: var(--white); white-space: nowrap; }
  .card--front .brand { left: 148px; top: 130px; }
  .card--back .brand { left: 20px; top: 97px; }

  .person { position: absolute; right: 20px; top: 30px; text-align: right; font-family: "Tinos", serif; }
  .person__name { font-size: 31px; line-height: 1; }
  .person__role { font-size: 13px; color: var(--neon); line-height: 1.3; }

  .contacts { position: absolute; left: 0; right: 0; top: 172px; height: 106px; background: var(--panel); }
  .contact { position: absolute; display: flex; align-items: center; font-size: 13px; white-space: nowrap; }
  .contact svg { width: 16px; height: 16px; fill: var(--neon); flex: none; }
  .contact--address { left: 12px; top: 25px; gap: 8px; font-size: 12.5px; letter-spacing: -0.2px; }
  .contact--phone { left: 12px; top: 75px; gap: 8px; }
  .contact--email { left: 326px; top: 24px; gap: 18px; }
  .contact--fax { left: 326px; top: 70px; gap: 18px; }

  .hours { position: absolute; left: 0; right: 0; top: 278px; height: 25px; background: var(--strip);
           font-size: 13px; color: var(--grey); }
  .hours span { position: absolute; top: 3px; white-space: nowrap; }
  .hours .weekdays { left: 12px; }
  .hours .sep-1 { left: 196px; }
  .hours .saturday { left: 238px; }
  .hours .sep-2 { left: 406px; }
  .hours .sunday { right: 16px; }

  .website { position: absolute; right: 8px; bottom: 6px; font-size: 13px; color: var(--white); }
</style>
</head>
<body>

<section class="card card--front">
  <div class="brand">
    <span class="brand__dot"></span>
    <span class="brand__name">Kip's Pharmacy</span>
  </div>
  <div class="band-green"></div>
</section>

<section class="card card--back">
  <div class="person">
    <div class="person__name">Rolf Mayhew</div>
    <div class="person__role">Owner/Pharm D</div>
  </div>

  <div class="brand">
    <span class="brand__dot"></span>
    <span class="brand__name">Kip's Pharmacy</span>
  </div>

  <div class="contacts">
    <div class="contact contact--address">
      <svg viewBox="0 0 24 24" aria-hidden="true"><path d="M12 2 1 12h3v10h6v-6h4v6h6V12h3z"/></svg>
      <span>7314 N Birchwood Rd Sioux Falls, SD 57193</span>
    </div>
    <div class="contact contact--phone">
      <svg viewBox="0 0 24 24" aria-hidden="true"><path d="M6.6 10.8a15.1 15.1 0 0 0 6.6 6.6l2.2-2.2c.3-.3.7-.4 1-.2 1.1.4 2.3.6 3.6.6.6 0 1 .4 1 1V20c0 .6-.4 1-1 1A17 17 0 0 1 3 4c0-.6.4-1 1-1h3.5c.6 0 1 .4 1 1 0 1.3.2 2.5.6 3.6.1.3 0 .7-.2 1z"/></svg>
      <span>605-318-2067</span>
    </div>
    <div class="contact contact--email">
      <svg viewBox="0 0 24 24" aria-hidden="true"><path d="M2 5h20v14H2zm2 2v.4l8 5.6 8-5.6V7z"/></svg>
      <span>kip@kipsrxhall.com</span>
    </div>
    <div class="contact contact--fax">
      <svg viewBox="0 0 24 24" aria-hidden="true"><path d="M6 2h12v5H6zM3 8h18v9h-3v5H6v-5H3zm5 7v5h8v-5z"/></svg>
      <span>605-318-2063</span>
    </div>
  </div>

  <div class="hours">
    <span class="weekdays">Monday-Friday 8am-7 pm</span>
    <span class="sep-1">.</span>
    <span class="saturday">Saturday 8am-12 pm</span>
    <span class="sep-2">.</span>
    <span class="sunday">Sunday Closed</span>
  </div>

  <div class="band-green"></div>
  <div class="website">www.kipsrxhall.com</div>
</section>

</body>
</html>
```